Premium Personal Brand — Facebook Banner (Used Across All Platforms)

Update — Additional Color Direction
In addition to the dark charcoal/slate direction already described, I'm also interested in seeing variants with:
Dark navy blue — Deep, authoritative, intelligence-community feel. Same textured/matte treatment, not flat or bright.
Warm charcoal with steel blue accent — Keep the dark base but introduce a subtle steel blue gradient, accent line, or tonal shift. Sophisticated, modern, adds dimension without adding color noise.
Both should maintain the same premium, restrained, architectural feel described in the original brief. No bright blues, no corporate PowerPoint energy — think midnight, think depth, think weight.
Everything else in the brief remains the same.
I am building a premium personal brand as an executive advisor to founders ($5M+ revenue).
This contest is Facebook-banner–focused, but the design must represent a visual system that will be reused across:
- LinkedIn
- YouTube
I- nstagram
- X (Twitter)
- Website hero sections and other brand touchpoints
Think of the Facebook banner as the primary expression of the brand — not a one-off graphic.
This project is about discovering a high-end visual style and brand feel, not decoration.
What to design
Please submit one cohesive visual system, shown primarily as:
- Facebook banner (primary focus)
The same design language should clearly translate to all platforms listed above.
Designers are responsible for using the current recommended dimensions for each platform.
Quick clarification on background direction:
Backgrounds should have depth and texture, not flat color fields. Avoid pure white, light grey, or solid black backgrounds. Think matte, architectural materials — stone, graphite, concrete, steel — not blank canvases. Subtle tonal variation is encouraged. Obvious gradients or decorative patterns are not.
Text to use
Primary Headline:
- Your Business Is Too Valuable To Be Run On Hope.
Subheadline:
- You didn’t build a business to become its prisoner.
Name:
Milo Verant
The headline should be the dominant visual element.
Logo note (important)
My personal logo is currently being finalized.
For this contest:
- Use a simple “MV” monogram placeholder
- Clean, bold, geometric sans-serif
- Do not design a logo
- The winning design must allow an easy logo swap later.
Headshot note (important)
- Please do not include a headshot in the banner design.
- Most platforms display a circular profile image separately.
- The banner should stand on its own using typography, layout, and tone only.
- Design the banner assuming the profile photo will sit nearby, not inside the banner.
Style direction
The design should feel:
- Premium
- Calm
- Confident
- Restrained
- High-trust
- Dark, neutral backgrounds are preferred.
- Fewer elements are better than more.
Think:
- Owner-level advisor
- Private equity / boardroom tone
- Industrial, Modern, Minimalist, Elite, Architectural, not decorative
What to avoid
Please do not submit designs that feel:
- Promotional, hype-driven, or salesy
- Like a coach, guru, or agency
- Bright, colorful, or gradient-heavy
- Busy or over-designed
- Based on stock photos
- No motivational speaker energy.
Reaction test
- If someone sees this banner on Facebook (or later on LinkedIn, YouTube, etc.), the reaction should be:
“That person is serious. I’d trust them with important decisions.”
Final note
- I am not looking for many variations.
- I am looking for one strong visual direction you believe in.
Simple beats clever.
- Restraint beats decoration.

```html
<!DOCTYPE html>
<html lang="en">
<head>
<meta charset="utf-8">
<title>Milo Verant — Facebook Cover</title>
<link rel="stylesheet" href="https://fonts.googleapis.com/css2?family=Inter:ital,wght@0,400;0,500;1,400&display=swap">
<style>
  :root {
    --page-bg: #ffffff;
    --navy-deep: #072846;
    --navy-mid: #0c3a64;
    --navy-light: #114673;
    --text-white: #ffffff;
    --text-soft: #e6edf5;
    --rule: rgba(255, 255, 255, 0.7);
  }
  * { box-sizing: border-box; margin: 0; padding: 0; }
  html, body {
    width: 1200px;
    height: 1200px;
    overflow: hidden;
    background: var(--page-bg);
  }
  .canvas {
    position: relative;
    width: 1200px;
    height: 1200px;
  }
  .cover {
    position: absolute;
    left: 40px;
    top: 350px;
    width: 1120px;
    height: 500px;
    overflow: hidden;
  }
  .cover-surface {
    position: absolute;
    inset: 0;
    background:
      radial-gradient(ellipse at 35% 40%, var(--navy-light) 0%, transparent 60%),
      radial-gradient(ellipse at 85% 80%, var(--navy-deep) 0%, transparent 55%),
      linear-gradient(160deg, var(--navy-mid) 0%, var(--navy-deep) 100%);
  }
  .cover-copy {
    position: absolute;
    left: 337px;
    top: 140px;
    color: var(--text-white);
    font-family: "Inter", sans-serif;
  }
  .headline {
    font-weight: 500;
    font-size: 51px;
    line-height: 50px;
    letter-spacing: -0.025em;
  }
  .subheadline {
    margin-top: 12px;
    margin-left: 5px;
    font-style: italic;
    font-weight: 400;
    font-size: 23px;
    letter-spacing: -0.02em;
    color: var(--text-soft);
  }
  .signature {
    margin-top: 34px;
    margin-left: 5px;
    width: 201px;
    padding: 10px 0 9px;
    border-top: 1px solid var(--rule);
    border-bottom: 1px solid var(--rule);
    font-weight: 500;
    font-size: 21px;
    letter-spacing: 0.32em;
    white-space: nowrap;
  }
</style>
</head>
<body>
  <main class="canvas">
    <section class="cover">
      <div class="cover-surface" role="img" aria-label="Deep navy textured matte background with faint thin gold hexagon outlines"></div>
      <div class="cover-copy">
        <h1 class="headline">Your business is too<br>valuable to be run on hope.</h1>
        <p class="subheadline">You didn’t build a business to become its prisoner.</p>
        <p class="signature">MILO VERANT</p>
      </div>
    </section>
  </main>
</body>
</html>
```